Modern Lawfirm Business Card Design

We're looking for a business card to incorporate the newly created logo we had made.

Ideally looking for a law firm business card demonstrating, modern, minimalist, strong/bold design.

I'm open to any design honestly, but nothing "flashy".

Target Market(s)

Immigration law, family immigration, humanitarian, general legal

Industry/Entity Type

Law Firm

Contact Information for Business Card

Please use dummy information, name, street address, city, state, phone number, email, website.

Font styles to use
Serif
Sans Serif

Requirements
Must have
• Please use dummy information, name, street address, city, state, phone number, email, website.

```html
<!DOCTYPE html>
<html lang="en">
<head>
<meta charset="utf-8">
<title>Valdero Immigration Law – Business Card</title>
<link rel="stylesheet" href="https://fonts.googleapis.com/css2?family=Roboto:wght@400;500;700&display=swap">
<style>
  :root {
    --backdrop: #2b2b2b;
    --card-white: #f1f1f1;
    --brand-blue: #1b5c9a;
    --text-grey: #5a5a5a;
    --title-grey: #7a7a7a;
    --rule-grey: #9a9a9a;
    --white: #ffffff;
  }
  * { margin: 0; padding: 0; box-sizing: border-box; }
  html, body {
    width: 1200px; height: 960px; overflow: hidden;
    background: var(--backdrop);
    font-family: "Roboto", Arial, sans-serif;
  }
  .canvas { position: relative; width: 1200px; height: 960px; }
  .card {
    position: absolute; width: 600px; height: 343px;
    box-shadow: 0 4px 10px rgba(0,0,0,0.5);
  }
  .card-front { left: 314px; top: 113px; background: var(--card-white); }
  .card-back { left: 311px; top: 472px; background: var(--brand-blue); }

  .brand-name {
    position: absolute; text-transform: uppercase; font-weight: 700;
    line-height: 1;
  }
  .card-front .brand-name {
    right: 48px; top: 48px; color: var(--brand-blue); text-align: right;
  }
  .card-back .brand-name {
    left: 0; right: 0; top: 134px; color: var(--white); text-align: center;
  }
  .brand-word { display: block; font-size: 38px; letter-spacing: 2px; }
  .card-back .brand-word { font-size: 50px; letter-spacing: 3px; }
  .brand-sub { display: block; font-size: 10px; letter-spacing: 5px; margin-top: 6px; }
  .card-back .brand-sub { font-size: 12px; letter-spacing: 7px; margin-top: 8px; }

  .holder { position: absolute; left: 42px; top: 186px; }
  .holder-name { color: var(--brand-blue); font-size: 22px; font-weight: 500; }
  .holder-title { color: var(--title-grey); font-size: 17px; margin-top: 1px; }

  .contact-list {
    position: absolute; left: 42px; top: 248px; list-style: none;
    color: var(--text-grey); font-size: 14px;
  }
  .contact-list li { display: flex; align-items: center; height: 21px; }
  .contact-list svg { width: 13px; height: 13px; margin-right: 8px; fill: var(--brand-blue); }

  .address {
    position: absolute; left: 214px; top: 274px; padding-left: 17px;
    border-left: 1px solid var(--rule-grey);
    color: var(--text-grey); font-size: 14px; line-height: 18px;
  }
  .back-web {
    position: absolute; left: 0; right: 0; top: 295px; text-align: center;
    color: var(--white); font-size: 13px; letter-spacing: 3px;
  }
  .back-web strong { font-weight: 700; }
</style>
</head>
<body>
<div class="canvas">
  <section class="card card-front">
    <div class="brand-name">
      <span class="brand-word">Valdero</span>
      <span class="brand-sub">Immigration Law</span>
    </div>
    <div class="holder">
      <div class="holder-name">MARK ELLISON</div>
      <div class="holder-title">President</div>
    </div>
    <ul class="contact-list">
      <li>
        <svg viewBox="0 0 24 24"><path d="M6.6 10.8a15 15 0 0 0 6.6 6.6l2.2-2.2a1 1 0 0 1 1-.25 11.4 11.4 0 0 0 3.6.57 1 1 0 0 1 1 1V20a1 1 0 0 1-1 1A17 17 0 0 1 3 4a1 1 0 0 1 1-1h3.5a1 1 0 0 1 1 1c0 1.25.2 2.45.57 3.57a1 1 0 0 1-.25 1z"/></svg>
        555 210 4870
      </li>
      <li>
        <svg viewBox="0 0 24 24"><path d="M2 5h20v14H2z M2 5l10 7 10-7" /><path d="M3 6l9 6 9-6v-1H3z" fill="#f1f1f1"/></svg>
        mark@valdero.com
      </li>
      <li>
        <svg viewBox="0 0 24 24"><circle cx="12" cy="12" r="10"/><path d="M2 12h20M12 2c3 3 3 17 0 20M12 2c-3 3-3 17 0 20" stroke="#f1f1f1" stroke-width="1.5" fill="none"/></svg>
        www.valdero.com
      </li>
    </ul>
    <div class="address">1240 Harbor View Road<br>Juneau, Alaska 99801</div>
  </section>

  <section class="card card-back">
    <div class="brand-name">
      <span class="brand-word">Valdero</span>
      <span class="brand-sub">Immigration Law</span>
    </div>
    <div class="back-web">www.<strong>valdero</strong>.com</div>
  </section>
</div>
</body>
</html>
```